Design für Auto-Folierung, Lieferwagen Tischlerei

Design für Lieferwagen Valbrand Kurier mit Kofferaufbau.
(Valbrand Kurier 428TXL Koffer 4325 Farbe weiß, Baujahr 2020)
Es sollte vom Design zu Holz, Möbel, Tischler, Firmenlogo passen.
Farben sollten zum Firmenlogo und der Wagenfarbe passen.
Es sollte modern und zeitlos sein.
Zusätzlicher Text und Bilder können verwendet werden.
Es würde vermutlich reichen den Aufbau und Motorhaube zu folieren, bin aber für alles offen.
Integriert werden sollte: Firmenlogo (rundum) und Anschrift (hinten) .

• Logo, Anschrift

```html
<!DOCTYPE html>
<html lang="de">
<head>
<meta charset="utf-8">
<title>Hagen Tischlerei – Fahrzeugbeschriftung</title>
<link href="https://fonts.googleapis.com/css2?family=Poppins:wght@500;600;700&family=Oswald:wght@500&display=swap" rel="stylesheet">
<style>
  :root {
    --navy: #14173f;
    --gold-light: #f0d98a;
    --gold: #c9a53a;
    --gold-dark: #9c7a1c;
    --white: #ffffff;
    --stage: #eef0f2;
  }
  * { margin: 0; padding: 0; box-sizing: border-box; }
  html, body { width: 1200px; height: 1200px; overflow: hidden; background: var(--stage); }
  .canvas { position: relative; width: 1200px; height: 1200px; }
  .wrap-panel {
    position: absolute; left: 100px; width: 1000px; height: 520px;
    background: var(--white); overflow: hidden;
    box-shadow: 0 2px 10px rgba(0,0,0,.12);
  }
  .wrap-panel--classic { top: 50px; }
  .wrap-panel--bold { top: 620px; }
  .gold-fill { background: linear-gradient(115deg, var(--gold-dark) 0%, var(--gold-light) 35%, var(--gold) 60%, var(--gold-light) 80%, var(--gold-dark) 100%); }
  .brand-mark { position: absolute; background: var(--navy); }
  .brand-name {
    position: absolute; font-family: "Poppins", sans-serif; font-weight: 600;
    color: var(--navy); line-height: 1; letter-spacing: 6px;
  }
  .brand-name span { display: block; }
  .band-svg { position: absolute; left: 0; top: 0; }
  .contact-line {
    position: absolute; left: 0; width: 100%; text-align: center;
    font-family: "Poppins", sans-serif; font-weight: 600; color: var(--navy);
  }
  .service-strip {
    position: absolute; background: var(--navy); color: var(--gold-light);
    font-family: "Oswald", sans-serif; font-weight: 500; text-transform: uppercase;
    display: flex; align-items: center; justify-content: center; white-space: nowrap;
  }
  .contact-box {
    position: absolute; display: flex; flex-direction: column; align-items: center; justify-content: center;
    font-family: "Poppins", sans-serif; color: var(--navy);
  }
  .contact-box .phone { font-weight: 600; font-size: 40px; }
  .contact-box .web { font-weight: 500; font-size: 30px; }
</style>
</head>
<body>
<main class="canvas">

  <section class="wrap-panel wrap-panel--classic">
    <svg class="band-svg" width="1000" height="520" viewBox="0 0 1000 520">
      <defs>
        <linearGradient id="goldBand" x1="0" y1="0" x2="1" y2="0.3">
          <stop offset="0" stop-color="#9c7a1c"/>
          <stop offset=".35" stop-color="#f0d98a"/>
          <stop offset=".6" stop-color="#c9a53a"/>
          <stop offset=".8" stop-color="#f0d98a"/>
          <stop offset="1" stop-color="#9c7a1c"/>
        </linearGradient>
      </defs>
      <path d="M0 270 C250 300 420 340 520 345 C640 340 820 290 1000 265 L1000 520 L0 520 Z" fill="url(#goldBand)"/>
      <path d="M0 300 C250 325 420 350 520 352 C640 350 820 320 1000 300" fill="none" stroke="#ffffff" stroke-width="5"/>
    </svg>
    <div class="brand-mark" style="left:120px; top:60px; width:170px; height:170px;"></div>
    <div class="brand-name" style="left:330px; top:62px;">
      <span style="font-size:118px;">HAGEN</span>
      <span style="font-size:52px; margin-top:16px; letter-spacing:8px;">TISCHLEREI</span>
    </div>
    <p class="contact-line" style="top:360px; font-size:34px;">+43 660 5183472 | www.hagen-tischlerei.at</p>
    <div class="service-strip" style="left:0; top:415px; width:100%; height:40px; font-size:22px; letter-spacing:.5px;">
      Küche • Esszimmer • Wohnzimmer • Schlafzimmer • Bad • Verschiedenes
    </div>
  </section>

  <section class="wrap-panel wrap-panel--bold">
    <div class="brand-mark" style="left:40px; top:40px; width:300px; height:440px;"></div>
    <div class="brand-name" style="left:450px; top:45px;">
      <span style="font-size:120px;">HAGEN</span>
      <span style="font-size:62px; margin-top:12px; letter-spacing:6px;">TISCHLEREI</span>
    </div>
    <div class="service-strip" style="left:440px; top:268px; width:540px; height:30px; font-size:15px;">
      Küche • Esszimmer • Wohnzimmer • Schlafzimmer • Bad • Verschiedenes
    </div>
    <div class="contact-box gold-fill" style="left:440px; top:315px; width:540px; height:170px;">
      <span class="phone">+43 660 5183472</span>
      <span class="web">www.hagen-tischlerei.at</span>
    </div>
  </section>

</main>
</body>
</html>
```